Project, Programme and Portfolio Management Consultant needs a business card

I have recently had someone create a brand guide for me and I wish to have new business cards that incorporate the new brand. I am an independent management consultant working with businesses to improve their ability to deliver their business strategy through selecting the right project, the right people and doing it in the right way. Whilst I am currently working on my own, I am hoping to start to build win business where I need to bring in a team and this branding activity is the start of that process.

Target Market(s)

Medium to large businesses, government departments and defence

Contact Information for Business Card

Name
job title
business name
mobile
email
website
linkedIn profile

Font styles to use
Other font styles liked:
• roboto light

Colors

Designer to choose colors to be used in the design.

Requirements
Must have
• Must use my logo and brand colours (see attached brand guide)

```html
<!DOCTYPE html>
<html lang="en">
<head>
<meta charset="utf-8">
<title>Kestrell Business Card</title>
<link href="https://fonts.googleapis.com/css2?family=Montserrat:wght@400;500&family=Roboto:wght@300;500&display=swap" rel="stylesheet">
<style>
  :root {
    --backdrop: #1a1a1a;
    --card: #161616;
    --card-edge: #222222;
    --foil: #bdbdbd;
    --foil-bright: #d6d6d6;
  }
  * { margin: 0; padding: 0; box-sizing: border-box; }
  html, body { width: 1200px; height: 900px; overflow: hidden; }
  body {
    background: radial-gradient(ellipse at 50% 40%, #2a2a2a 0%, var(--backdrop) 70%);
    font-family: "Montserrat", sans-serif;
    color: var(--foil);
  }
  .stage {
    width: 1200px; height: 900px;
    display: flex; flex-direction: column; align-items: center; justify-content: center;
    gap: 28px;
  }
  .card {
    width: 640px; height: 366px;
    background: linear-gradient(135deg, #1c1c1c 0%, var(--card) 60%, #1e1e1e 100%);
    border: 1px solid var(--card-edge);
    box-shadow: 0 18px 40px rgba(0,0,0,0.55);
    position: relative;
  }
  .card-front { display: flex; align-items: center; justify-content: center; }
  .brand-name {
    font-family: "Montserrat", sans-serif;
    font-weight: 500;
    font-size: 44px;
    letter-spacing: 6px;
    color: var(--foil-bright);
  }
  .card-back {
    display: flex; align-items: center; justify-content: center;
    padding-top: 40px;
  }
  .identity {
    text-align: right;
    padding-right: 26px;
    font-size: 15px;
    line-height: 1.35;
  }
  .person-name {
    font-family: "Roboto", sans-serif;
    font-size: 25px;
    letter-spacing: 1.5px;
    text-transform: uppercase;
    color: var(--foil-bright);
    margin-bottom: 4px;
  }
  .person-name .first { font-weight: 300; }
  .person-name .last { font-weight: 500; }
  .role { font-weight: 500; }
  .divider {
    width: 1.5px; height: 96px;
    background: var(--foil);
  }
  .contacts {
    list-style: none;
    padding-left: 26px;
    font-size: 15px;
    line-height: 1.5;
  }
  .contacts li { display: flex; align-items: center; gap: 12px; }
  .contacts svg { width: 13px; height: 13px; flex: none; }
</style>
</head>
<body>
<main class="stage">
  <section class="card card-front">
    <span class="brand-name">KESTRELL</span>
  </section>

  <section class="card card-back">
    <div class="identity">
      <h1 class="person-name"><span class="first">Daniel</span> <span class="last">Hart</span></h1>
      <p class="role">Director</p>
      <p class="address">48 Marlow Street<br>Kensal Town London W10 4QT</p>
    </div>
    <div class="divider"></div>
    <ul class="contacts">
      <li>
        <svg viewBox="0 0 16 16" aria-hidden="true"><path d="M4 1.5l2.3 2.8-1.4 1.6a9 9 0 0 0 5.2 5.2l1.6-1.4 2.8 2.3-1.6 2.2C7.5 14 2 8.5 1.8 3.1z" fill="none" stroke="currentColor" stroke-width="1.4" stroke-linejoin="round"/></svg>
        +44 7700 900512
      </li>
      <li>
        <svg viewBox="0 0 16 16" aria-hidden="true"><rect x="1.5" y="3.5" width="13" height="9" fill="none" stroke="currentColor" stroke-width="1.4"/><path d="M1.5 3.5L8 9l6.5-5.5" fill="none" stroke="currentColor" stroke-width="1.4"/></svg>
        info@kestrell.com
      </li>
      <li>
        <svg viewBox="0 0 16 16" aria-hidden="true"><circle cx="8" cy="8" r="6.3" fill="none" stroke="currentColor" stroke-width="1.3"/><ellipse cx="8" cy="8" rx="2.7" ry="6.3" fill="none" stroke="currentColor" stroke-width="1.1"/><path d="M1.7 8h12.6M2.6 5h10.8M2.6 11h10.8" stroke="currentColor" stroke-width="1"/></svg>
        www.kestrell.com
      </li>
      <li>
        <svg viewBox="0 0 16 16" aria-hidden="true"><rect x="2" y="2" width="12" height="12" fill="currentColor"/></svg>
        in/kestrell-4521
      </li>
    </ul>
  </section>
</main>
</body>
</html>
```